BLUE & AMBER SALVE TOPICAL BOX + LABELS TO MATCH

Hello ! I hope you're up to helping with my designs again. I appreciate all your help.
I have two topicals needing redesign.
Box + Label , once the box is together, we can slap the labels together easy.
I have CBD version and THC version of both these balms, so well start w THC, then lay out the CBD. It should be eaay with few minor differences.
PLEASE USE only tHE SMALL BOX TEMPLATE,
Anyway, once the boxes are complete, I need to revise the label to match the boxes.
1.
AMBER SALVE :
(this box color I would like orange, like a jack-o-lantern (i uploaded our current label so you can match it)
KORVEX logo outlined in Gold (on LID)
(I uploaded a picture of what the oulined logo looks like)
THC SYMBOL
AMBER SALVE (GOLD) (on Front)
HIGHLY NUTRITIOUS POWERFUL THC RELIEF
net wt. 2 oz (56 g)
SIDE PANEL :
ORGANIC INGREDIENTS : Butyrospermum Parkii Butter (Shea Butter), Persia Gratissima (Avocado) Oil, Simmondsia chinesis (Gold Jojoba) Oil , Vitus Vinifera (Grape) Seed Oil, Arnica montana (Arnica) and Symphytum officinalis (Comfrey Leaf) macerated in Sunflower Oil, Calophyllum inophyllum (Tamanu) Oil, Nigella sativa (Black Seed) Oil, Locally Harvested Beeswax, THC CANNABIS EXTRACT, Pure Cannabigerol (CBG), Proprietary Blend of Therapeutic Essential Oils (including but not limited to : Yarrow , Celery Seed , Tea Tree , Lavender , Helichrysum, Pine Scotch, Rosemary, Geranium), Tocopherol (Vitamin E, antioxidant )
Color is a Natural Result of Chamomile Steam-Distillation and May Vary in Intensity. Consistency can also Vary. For Optimal Preservation, Keep in a Cool, Dark Place. Fatty Acids may Naturally Aggregate when Exposed to Temperature Extremes Forming Beads. To Fix This, Use a Hair Dryer to Melt them Back to a Smooth Consistency.
BACK PANEL :
WARNING: THIS PRODUCT IS FOR USE BY INDIVIDUALS 21 YEARS OF AGE OR OLDER OR BY REGISTERED QUALIFYING PATIENTS ONLY. IT IS ILLEGAL TO DRIVE A MOTOR VEHICLE WHILE UNDER THE INFLUENCE OF MARIJUANA.
(Outlined Box )::
WARNING: USE BY PREGNANT OR BREASTFEEDING WOMEN OR BY WOMEN PLANNING TO BECOME PREGNANT, MAY RESULT IN FETAL INJURY, PRETERM BIRTH, LOW BIRTHWEIGHT, OR DEVELOPMENTAL PROBLEMS FOR THE CHILD.
KEEP OUT OF REACH OF CHILDREN.
CIVIC TOXIN RESPONSE BUREAU 1 800 555 0147
THE ACTUAL VALUE OF CANNABINOIDS MAY VARY FROM THE REPORTED VALUE BY +/- 10%
ACTIVATION TIME : 10 - 60 MINUTES
MADE IN A MARIJUANA FACILITY
PACKAGED BY
MILDRED’S HAZE Co.
KT-R-004817
www.FROSTLUMP.info
2.
TEAL SALVE
white box
KORVEX Gold out line, red w blue leaf
FRONT PANEL :
TEAL SALVE (blue)
net wt. 2 oz (56 g)
Ingredients : Butyrospermum Parkii Butter (Shea Butter), Aloe Barbadensis (Aloe Vera) Leaf Extract, Coco Nucifera (Coconut) Oil, THC CANNABIS EXTRACT, Cannabis Sativa Seed Oil, Pure Cannabidol (Hemp Extract), Prunes Armeniaca (Apricot) Kernal Oil, Hydrogenated Vegetable (Soybean) Oil, Prunus Amygdalus Dulcis (Sweet Almond Oil), Vitus Vinifera (Grape) Seed Oil, Macadamia Ternifolia Seed Oil, Daucus Carota (Carrot) Seed Oil, Proprietary Blend of Therapeutic Essential Oils (including but not limited to : Lavender, Chamomile), Tocopherol (Vitamin E, antioxidant)

```html
<!DOCTYPE html>
<html lang="en">
<head>
<meta charset="utf-8">
<title>KORVEX Teal Salve – Box Panels</title>
<link href="https://fonts.googleapis.com/css2?family=Oswald:wght@400;500;600&family=Roboto+Condensed:wght@300;400&family=Montserrat:wght@500&display=swap" rel="stylesheet">
<style>
  :root{
    --bg:#ede6dc;
    --panel:#ffffff;
    --panel-shade:#f3f3f3;
    --brand-red:#e8232a;
    --navy:#1f44a0;
    --mid-blue:#3d6bc2;
    --sky:#8cc3ec;
    --ink-blue:#2b4fa8;
    --reg-green:#2e8a55;
    --edge:#dcdcdc;
  }
  *{box-sizing:border-box;margin:0;padding:0}
  html,body{width:1200px;height:1200px;overflow:hidden}
  body{background:var(--bg);position:relative;font-family:"Roboto Condensed",sans-serif}

  .panel{position:absolute;width:480px;height:480px;background:var(--panel);
    border:1px solid var(--edge);overflow:hidden}
  .panel--lid{left:610px;top:90px}
  .panel--side{left:110px;top:590px;background:linear-gradient(135deg,var(--panel) 0%,var(--panel-shade) 100%)}
  .panel--front{left:610px;top:590px}

  .brand-stack{position:absolute;left:0;right:0;top:70px;text-align:center}
  .brand-name{font-family:"Oswald",sans-serif;font-weight:600;font-size:118px;line-height:1;
    color:var(--brand-red);letter-spacing:2px}
  .sub-brand{font-family:"Montserrat",sans-serif;font-weight:500;font-size:30px;letter-spacing:22px;
    color:var(--navy);margin-top:10px;padding-left:22px}
  .product-name{display:block;font-family:"Oswald",sans-serif;font-weight:500;font-size:104px;line-height:1;
    white-space:nowrap;margin-top:6px;transform:scaleY(1.35);transform-origin:top center;
    background:linear-gradient(90deg,var(--navy) 0%,var(--mid-blue) 35%,var(--sky) 55%,var(--mid-blue) 80%,var(--navy) 100%);
    -webkit-background-clip:text;background-clip:text;color:transparent}
  .net-weight{position:absolute;left:0;right:0;bottom:34px;text-align:center;
    font-family:"Roboto Condensed",sans-serif;font-size:20px;color:var(--ink-blue)}

  .reg-mark{position:absolute;top:18px;right:18px;width:70px;height:64px}

  .badge-row{position:absolute;left:26px;right:26px;top:28px;display:flex;justify-content:space-between}
  .badge{width:100px;height:100px}
  .badge text{font-family:"Montserrat",sans-serif;font-weight:500;font-size:11px;letter-spacing:2px;fill:var(--ink-blue)}

  .description{position:absolute;left:34px;right:34px;top:160px;
    font-family:"Roboto Condensed",sans-serif;font-weight:300;font-size:21px;line-height:1.32;
    color:var(--ink-blue);text-align:justify}
</style>
</head>
<body>

<!-- Lid panel -->
<section class="panel panel--lid" aria-label="Lid panel">
  <div class="brand-stack">
    <div class="brand-name">KORVEX</div>
    <div class="sub-brand">BOTANIC</div>
    <span class="product-name">TEAL SALVE</span>
  </div>
</section>

<!-- Side panel -->
<section class="panel panel--side" aria-label="Side panel">
  <div class="badge-row">
    <svg class="badge" viewBox="0 0 100 100" aria-label="Organic ingredients">
      <defs>
        <path id="arcTop1" d="M14,50 A36,36 0 0 1 86,50"/>
        <path id="arcBot1" d="M12,50 A38,38 0 0 0 88,50"/>
      </defs>
      <circle cx="50" cy="50" r="46" fill="none" stroke="var(--ink-blue)" stroke-width="1.5"/>
      <text><textPath href="#arcTop1" startOffset="50%" text-anchor="middle">ORGANIC</textPath></text>
      <text><textPath href="#arcBot1" startOffset="50%" text-anchor="middle" dominant-baseline="hanging">INGREDIENTS</textPath></text>
      <path d="M38,62 C30,48 36,36 50,32 C52,46 48,56 38,62 Z" fill="var(--sky)" stroke="var(--ink-blue)" stroke-width="1.5"/>
      <path d="M50,64 C58,56 64,46 58,38 C48,44 46,56 50,64 Z" fill="#cfe4f7" stroke="var(--ink-blue)" stroke-width="1.5"/>
    </svg>
    <svg class="badge" viewBox="0 0 100 100" aria-label="High potency">
      <defs>
        <path id="arcTop2" d="M14,50 A36,36 0 0 1 86,50"/>
        <path id="arcBot2" d="M12,50 A38,38 0 0 0 88,50"/>
      </defs>
      <circle cx="50" cy="50" r="46" fill="none" stroke="var(--ink-blue)" stroke-width="1.5"/>
      <text><textPath href="#arcTop2" startOffset="50%" text-anchor="middle">HIGH</textPath></text>
      <text><textPath href="#arcBot2" startOffset="50%" text-anchor="middle" dominant-baseline="hanging">POTENCY</textPath></text>
      <path d="M53,34 L42,52 L50,52 L46,66 L58,46 L50,46 Z" fill="var(--sky)" stroke="var(--ink-blue)" stroke-width="1.5" stroke-linejoin="round"/>
      <g stroke="var(--ink-blue)" stroke-width="1.5" stroke-linecap="round">
        <line x1="34" y1="50" x2="29" y2="50"/><line x1="66" y1="50" x2="71" y2="50"/>
        <line x1="37" y1="38" x2="33" y2="34"/><line x1="63" y1="38" x2="67" y2="34"/>
        <line x1="37" y1="62" x2="33" y2="66"/><line x1="63" y1="62" x2="67" y2="66"/>
      </g>
    </svg>
    <svg class="badge" viewBox="0 0 100 100" aria-label="Award winning">
      <defs>
        <path id="arcTop3" d="M14,50 A36,36 0 0 1 86,50"/>
        <path id="arcBot3" d="M12,50 A38,38 0 0 0 88,50"/>
      </defs>
      <circle cx="50" cy="50" r="46" fill="none" stroke="var(--ink-blue)" stroke-width="1.5"/>
      <text><textPath href="#arcTop3" startOffset="50%" text-anchor="middle">AWARD</textPath></text>
      <text><textPath href="#arcBot3" startOffset="50%" text-anchor="middle" dominant-baseline="hanging">WINNING</textPath></text>
      <path d="M42,30 L50,48 M58,30 L50,48" stroke="var(--ink-blue)" stroke-width="1.5" fill="none"/>
      <circle cx="50" cy="56" r="10" fill="#cfe4f7" stroke="var(--ink-blue)" stroke-width="1.5"/>
      <text x="50" y="60" text-anchor="middle" style="font-size:11px;letter-spacing:0">1</text>
    </svg>
    <svg class="badge" viewBox="0 0 100 100" aria-label="Natural healing">
      <defs>
        <path id="arcTop4" d="M14,50 A36,36 0 0 1 86,50"/>
        <path id="arcBot4" d="M12,50 A38,38 0 0 0 88,50"/>
      </defs>
      <circle cx="50" cy="50" r="46" fill="none" stroke="var(--ink-blue)" stroke-width="1.5"/>
      <text><textPath href="#arcTop4" startOffset="50%" text-anchor="middle">NATURAL</textPath></text>
      <text><textPath href="#arcBot4" startOffset="50%" text-anchor="middle" dominant-baseline="hanging">HEALING</textPath></text>
      <path d="M50,36 C44,42 44,50 50,54 C56,50 56,42 50,36 Z" fill="var(--sky)" stroke="var(--ink-blue)" stroke-width="1.5"/>
      <path d="M34,60 L46,60 C52,60 56,62 62,58 L66,56" fill="none" stroke="var(--ink-blue)" stroke-width="1.5" stroke-linecap="round"/>
    </svg>
  </div>
  <p class="description">KORVEX TEAL SALVE is a harmonious synergy of botanial-rich actives embraced with natural and organic therapeutic oils overflowing with a high-content anti-inflammatory infusion and supercharged with THC. The intrinsic nature of this balm brings forth soothing relief and healing to the areas where you need it the most. The intelligence of this alchemized blend is characterized by its powerful relief and deeply calming comforts.</p>
</section>

<!-- Front panel -->
<section class="panel panel--front" aria-label="Front panel">
  <svg class="reg-mark" viewBox="0 0 70 64" role="img" aria-label="Regulatory product symbol">
    <path d="M4,4 L66,4 L35,60 Z" fill="#fff" stroke="var(--reg-green)" stroke-width="5" stroke-linejoin="round"/>
  </svg>
  <div class="brand-stack">
    <div class="brand-name">KORVEX</div>
    <div class="sub-brand">BOTANIC</div>
    <span class="product-name">TEAL SALVE</span>
  </div>
  <div class="net-weight">net wt. 2 oz (56 g)</div>
</section>

</body>
</html>
```